Letterhead Design for Law Firm that Specializes in Property Damage Litigation

We are looking for a redesign of our letterhead. Our current letterhead lists all of our current staff members and we'd like to come up with a design that does NOT list all of the staff members so that it does not need to be updated with every newly hired employee. Must be in editable format.

We are a law firm that specializes in property damage, so we need something that is professional, yet modern. The final design should use our existing logo and should use a blue color scheme (alternate colors would be gray, black, and white).

Industry/Entity Type

Legal

Colors
0054AA
0677BA
7BADD7
CADEEF
E8F1F8

```html
<!DOCTYPE html>
<html lang="en">
<head>
<meta charset="utf-8">
<title>Hartwell Ossen &amp; Pryce — Letterhead</title>
<link href="https://fonts.googleapis.com/css2?family=Marcellus&family=Marcellus+SC&family=Open+Sans:wght@400;600&display=swap" rel="stylesheet">
<style>
  :root {
    --blue-deep: #0054AA;
    --blue: #0677BA;
    --blue-soft: #7BADD7;
    --blue-pale: #CADEEF;
    --blue-mist: #E8F1F8;
    --ink: #3a3f47;
    --gray: #8a9099;
    --gray-light: #d7dbe0;
    --gray-band: #b9bec5;
    --paper: #ffffff;
  }
  * { box-sizing: border-box; margin: 0; padding: 0; }
  html, body { width: 849px; height: 1200px; overflow: hidden; background: var(--paper); }
  .letterhead {
    position: relative;
    width: 849px;
    height: 1200px;
    background: var(--paper);
    font-family: "Open Sans", Arial, sans-serif;
    color: var(--ink);
  }
  .brand {
    position: absolute;
    left: 62px;
    top: 118px;
  }
  .firm-name {
    display: flex;
    align-items: center;
    gap: 14px;
    font-family: "Marcellus", Georgia, serif;
    font-size: 30px;
    line-height: 1.1;
    color: var(--ink);
    letter-spacing: 1px;
  }
  .firm-name .mark {
    width: 22px;
    height: 22px;
    background: var(--blue);
    flex: none;
  }
  .tagline {
    margin-top: 6px;
    font-size: 11.5px;
    letter-spacing: 0.4px;
    color: var(--ink);
    text-transform: uppercase;
  }
  .backdrop-square {
    position: absolute;
    left: 610px;
    top: 890px;
    width: 200px;
    height: 180px;
    background: var(--blue-mist);
    opacity: 0.6;
  }
  .main-phone {
    position: absolute;
    left: 50px;
    top: 1082px;
    font-size: 28px;
    color: var(--ink);
  }
  .website {
    position: absolute;
    left: 50px;
    top: 1120px;
    font-size: 27px;
    color: var(--gray-light);
  }
  .office {
    position: absolute;
    top: 1072px;
    width: 170px;
    font-size: 10px;
    color: var(--gray);
  }
  .office.philadelphia { left: 334px; }
  .office.new-jersey { left: 512px; width: 190px; }
  .office h2 {
    font-family: "Marcellus SC", Georgia, serif;
    font-weight: 400;
    font-size: 15px;
    color: var(--ink);
    letter-spacing: 0.5px;
    margin-bottom: 5px;
  }
  .office ul { list-style: none; }
  .office li {
    display: flex;
    align-items: flex-start;
    gap: 7px;
    line-height: 15px;
    white-space: nowrap;
  }
  .office svg { flex: none; margin-top: 3px; }
  .footer-band {
    position: absolute;
    left: 0;
    bottom: 0;
    width: 849px;
    height: 34px;
  }
</style>
</head>
<body>
<main class="letterhead">
  <header class="brand">
    <div class="firm-name">
      <span class="mark"></span>
      <span>Hartwell Ossen &amp; Pryce</span>
    </div>
    <p class="tagline">The Property Damage Attorneys</p>
  </header>

  <div class="backdrop-square"></div>

  <footer>
    <p class="main-phone">(555) 310-4200</p>
    <p class="website">www.hoplegal.com</p>

    <section class="office philadelphia">
      <h2>Philadelphia Office</h2>
      <ul>
        <li><svg width="9" height="9" viewBox="0 0 10 10"><circle cx="5" cy="5" r="5" fill="var(--blue)"/></svg>555.310.4200</li>
        <li><svg width="9" height="9" viewBox="0 0 10 10"><circle cx="5" cy="5" r="5" fill="var(--blue)"/></svg>555.310.4299</li>
        <li><svg width="9" height="9" viewBox="0 0 10 10"><circle cx="5" cy="5" r="5" fill="var(--blue)"/></svg><span>2480 Market Crossing Suite 900<br>Philadelphia, PA 19100</span></li>
      </ul>
    </section>

    <section class="office new-jersey">
      <h2>New Jersey Office</h2>
      <ul>
        <li><svg width="9" height="9" viewBox="0 0 10 10"><circle cx="5" cy="5" r="5" fill="var(--blue)"/></svg>555.624.7180</li>
        <li><svg width="9" height="9" viewBox="0 0 10 10"><circle cx="5" cy="5" r="5" fill="var(--blue)"/></svg>555.310.4299</li>
        <li><svg width="9" height="9" viewBox="0 0 10 10"><circle cx="5" cy="5" r="5" fill="var(--blue)"/></svg><span>315 Linden Road North, Suite 110<br>Cherry Hill, NJ 08000</span></li>
      </ul>
    </section>

    <svg class="footer-band" viewBox="0 0 849 34" preserveAspectRatio="none">
      <rect x="0" y="0" width="849" height="34" fill="var(--blue-pale)"/>
      <polygon points="0,0 440,0 410,34 0,34" fill="var(--gray-band)"/>
    </svg>
  </footer>
</main>
</body>
</html>
```